Box Design of "pet rapid test for dogs & cats" with professional use

"The market is in Southeast Asia, South America, Europe, and the U.S."
Clients: Veterinary clinics, pet hospitals,(a small number of home use)

Primary colors:
Orange, Green,or Blue, (select 1,or 2 color)
Neutrals: Black, Gray, or White (optional)
Dimensions:135mm(L)*90mm(W)*105mm(W)

Kindly review the attached file for additional content
Updates

I have increased my budget, please provide a satisfactory design solution, thank you very much for your work.

Target Market(s)

Southeast Asia, South America, Europe, and the U.S.

Industry/Entity Type

Veterinary test kit for dogs & cats

Colors
0054AA
0677BA
7BADD7
CADEEF
E8F1F8
0094D4
00A9DD
6FCCEA
C7EBF8
E9F6FB
00AB8E
00BBA5
67D7C9
C6EFE9
E9F9F6
59FF00
82FF00
B8FF75
E3FFCB
F4FFEA
F0912C
F2A743
F7CA91
FBE8D2
FDF5EE
EE7325
F08F49
F5BC92
FAE3D3
FDF4ED

Requirements
Nice to have
• Appealing Box Appearance with professional

```html
<!DOCTYPE html>
<html lang="en">
<head>
<meta charset="utf-8">
<title>PawSure – Pet Rapid Test Kit Packaging</title>
<link rel="stylesheet" href="https://fonts.googleapis.com/css2?family=Fredoka:wght@500;600&family=Anton&family=Open+Sans:wght@400;600;700&family=Quicksand:wght@500&display=swap">
<style>
  :root{
    --green:#3ea318;
    --lime:#6fd900;
    --lime-dark:#4fa300;
    --ink:#0f1c1b;
    --charcoal:#2b3b39;
    --paper:#ffffff;
    --bg-top:#ffffff;
    --bg-bottom:#dcdcdc;
    --text-dark:#2a2a2a;
    --photo-a:#d9b07a;
    --photo-b:#8c7f74;
  }
  html,body{margin:0;padding:0;overflow:hidden;}
  .canvas{
    position:relative;width:1200px;height:1200px;overflow:hidden;
    background:linear-gradient(180deg,var(--bg-top) 0%,#f1f1f1 55%,var(--bg-bottom) 100%);
    font-family:"Open Sans",sans-serif;
  }
  .brand-block{position:absolute;left:85px;top:250px;}
  .brand-name{
    display:flex;align-items:center;gap:18px;
    font-family:"Fredoka",sans-serif;font-weight:600;font-size:96px;line-height:1;
    color:var(--green);
  }
  .brand-dot{width:46px;height:46px;border-radius:50%;background:var(--charcoal);}
  .brand-tagline{
    margin-top:14px;font-family:"Fredoka",sans-serif;font-weight:500;
    font-size:23px;color:var(--green);
  }
  .section-title{
    position:absolute;left:47px;top:722px;margin:0;
    font-family:"Quicksand",sans-serif;font-weight:500;font-size:36px;
    color:var(--text-dark);
  }
  .dieline-sheet{
    position:absolute;left:42px;top:775px;width:512px;height:292px;background:var(--paper);
  }
  .dieline-sheet svg,.front-panel svg{display:block;}
  .dimensions{
    position:absolute;right:34px;top:10px;font-size:11px;color:var(--text-dark);
    font-family:"Open Sans",sans-serif;
  }
  .front-panel{
    position:absolute;left:610px;top:640px;width:540px;height:420px;
    box-shadow:0 18px 40px rgba(0,0,0,.18);
  }
  .t-brand{font-family:"Fredoka",sans-serif;font-weight:600;}
  .t-title{font-family:"Anton",sans-serif;}
  .t-body{font-family:"Open Sans",sans-serif;}
</style>
</head>
<body>
<main class="canvas">

  <section class="brand-block">
    <div class="brand-name"><span class="brand-dot"></span>PawSure</div>
    <div class="brand-tagline">Made for Pets, Backed by Vets</div>
  </section>

  <h2 class="section-title">Packaging sample</h2>

  <section class="dieline-sheet">
    <svg width="512" height="292" viewBox="0 0 825 470">
      <path d="M81 187 V32 a12 12 0 0 1 12-12 H275 a12 12 0 0 1 12 12 V187 Z" fill="var(--lime)"/>
      <circle cx="165" cy="118" r="8" fill="var(--paper)"/>
      <text x="183" y="137" text-anchor="middle" class="t-brand" font-size="14" fill="var(--paper)">PawSure</text>
      <text x="183" y="147" text-anchor="middle" class="t-body" font-size="5" fill="var(--paper)">Made for Pets, Backed by Vets</text>
      <path d="M50 190 L81 187 V347 L50 344 Z" fill="var(--lime)"/>
      <rect x="81" y="187" width="206" height="160" fill="var(--ink)"/>
      <polygon points="81,187 165,187 150,347 81,347" fill="var(--paper)"/>
      <polygon points="170,187 287,187 287,212 180,212" fill="var(--lime)"/>
      <rect x="81" y="270" width="75" height="77" fill="var(--photo-a)" role="img" aria-label="Photo of a golden retriever and a tabby cat"/>
      <text x="123" y="245" text-anchor="middle" class="t-brand" font-size="10" fill="var(--green)">PawSure</text>
      <text x="280" y="203" text-anchor="end" class="t-brand" font-size="8" fill="var(--paper)">Made for Pets · Backed by Vets</text>
      <text x="188" y="247" class="t-title" font-size="15" fill="var(--paper)">PET RAPID</text>
      <text x="188" y="264" class="t-title" font-size="16" fill="var(--lime)">TEST KIT</text>
      <rect x="188" y="268" width="76" height="10" fill="none" stroke="var(--lime)" stroke-width="1"/>
      <text x="226" y="276" text-anchor="middle" class="t-body" font-weight="700" font-size="5.5" fill="var(--paper)">FOR DOGS AND CATS</text>
      <text x="165" y="292" class="t-body" font-size="4.5" fill="var(--lime)">Contents :</text>
      <text x="165" y="300" class="t-body" font-size="4" fill="var(--paper)">• Test Kits (Cassette, disposable dropper, desiccant)</text>
      <text x="165" y="307" class="t-body" font-size="4" fill="var(--paper)">• Assay buffer.  • Sterile swabs.</text>
      <text x="165" y="314" class="t-body" font-size="4" fill="var(--paper)">• Instruction manual.</text>
      <g fill="var(--lime)"><circle cx="170" cy="334" r="5"/><circle cx="184" cy="334" r="5"/><circle cx="198" cy="334" r="5"/><circle cx="212" cy="334" r="5"/><circle cx="226" cy="334" r="5"/></g>
      <rect x="250" y="326" width="32" height="14" fill="var(--paper)"/>
      <path d="M290 187 V130 a8 8 0 0 1 8-8 H414 a8 8 0 0 1 8 8 V187 Z" fill="var(--lime)"/>
      <rect x="287" y="187" width="137" height="160" fill="var(--ink)"/>
      <circle cx="322" cy="208" r="5" fill="var(--lime)"/>
      <text x="331" y="212" class="t-brand" font-size="10" fill="var(--paper)">PawSure</text>
      <text x="355" y="320" text-anchor="middle" class="t-body" font-weight="700" font-size="4.5" fill="var(--paper)">MADE by NORVEL LABS</text>
      <text x="355" y="327" text-anchor="middle" class="t-body" font-size="4" fill="var(--paper)">Made for Pets, Backed by Vets</text>
      <polygon points="370,335 424,330 424,347 362,347" fill="var(--paper)"/>
      <text x="420" y="343" text-anchor="end" class="t-body" font-size="3.5" fill="var(--ink)">+01 555 0100 22</text>
      <rect x="424" y="187" width="205" height="160" fill="var(--ink)"/>
      <polygon points="424,187 505,187 490,347 424,347" fill="var(--paper)"/>
      <polygon points="508,187 629,187 629,212 518,212" fill="var(--lime)"/>
      <rect x="424" y="275" width="90" height="72" fill="var(--photo-a)" role="img" aria-label="Photo of a puppy and kittens"/>
      <text x="463" y="245" text-anchor="middle" class="t-brand" font-size="10" fill="var(--green)">PawSure</text>
      <text x="620" y="203" text-anchor="end" class="t-body" font-weight="700" font-size="5.5" fill="var(--paper)">Hecho para mascotas</text>
      <text x="528" y="247" class="t-title" font-size="10" fill="var(--paper)">KIT DE PRUEBA RÁPIDA</text>
      <text x="528" y="259" class="t-title" font-size="10" fill="var(--lime)">PARA MASCOTAS</text>
      <rect x="528" y="264" width="72" height="10" fill="none" stroke="var(--lime)" stroke-width="1"/>
      <text x="564" y="272" text-anchor="middle" class="t-body" font-weight="700" font-size="5" fill="var(--paper)">PERROS Y GATOS</text>
      <text x="518" y="290" class="t-body" font-size="4.5" fill="var(--lime)">Contenido:</text>
      <text x="518" y="298" class="t-body" font-size="4" fill="var(--paper)">• Kits de prueba y gotero</text>
      <text x="518" y="305" class="t-body" font-size="4" fill="var(--paper)">• Tampón • Hisopos • Manual</text>
      <g fill="var(--lime)"><circle cx="527" cy="334" r="5"/><circle cx="541" cy="334" r="5"/><circle cx="555" cy="334" r="5"/><circle cx="569" cy="334" r="5"/><circle cx="583" cy="334" r="5"/></g>
      <path d="M632 187 V130 a8 8 0 0 1 8-8 H763 V187 Z" fill="var(--lime)"/>
      <rect x="629" y="187" width="138" height="160" fill="var(--ink)"/>
      <circle cx="665" cy="208" r="5" fill="var(--lime)"/>
      <text x="674" y="212" class="t-brand" font-size="10" fill="var(--paper)">PawSure</text>
      <g class="t-body" font-size="4" fill="var(--paper)">
        <text x="640" y="232">Simple and fast for clinic use</text>
        <text x="640" y="242">Results in ten minutes</text>
        <text x="640" y="252">Accurate lateral flow method</text>
        <text x="640" y="262">Store dry and cool</text>
      </g>
      <text x="698" y="320" text-anchor="middle" class="t-body" font-weight="700" font-size="4.5" fill="var(--paper)">MADE by NORVEL LABS</text>
      <polygon points="712,335 767,330 767,347 704,347" fill="var(--paper)"/>
      <path d="M290 347 H424 V420 H362 a8 8 0 0 1-8-8 V395 Z" fill="var(--lime)"/>
      <path d="M424 347 H629 L585 420 V432 a8 8 0 0 1-8 8 H478 a8 8 0 0 1-8-8 V420 Z" fill="var(--lime)"/>
      <path d="M629 347 H767 L706 395 V412 a8 8 0 0 1-8 8 H629 Z" fill="var(--lime)"/>
    </svg>
    <div class="dimensions">长135mm×宽90mm×高105mm</div>
  </section>

  <section class="front-panel">
    <svg width="540" height="420" viewBox="0 0 540 420">
      <defs>
        <linearGradient id="photoTone" x1="0" y1="0" x2="1" y2="1">
          <stop offset="0" stop-color="var(--photo-b)"/>
          <stop offset="1" stop-color="var(--photo-a)"/>
        </linearGradient>
      </defs>
      <rect width="540" height="420" fill="var(--ink)"/>
      <polygon points="0,0 215,0 165,420 0,420" fill="var(--paper)"/>
      <polygon points="215,0 235,0 272,88 252,88" fill="var(--lime-dark)"/>
      <polygon points="235,0 540,0 540,88 272,88" fill="var(--lime)"/>
      <rect x="0" y="215" width="200" height="205" fill="url(#photoTone)" role="img" aria-label="Photo of a golden retriever resting beside a tabby cat"/>
      <circle cx="34" cy="140" r="10" fill="var(--charcoal)"/>
      <text x="52" y="150" class="t-brand" font-size="30" fill="var(--green)">PawSure</text>
      <text x="52" y="164" class="t-body" font-size="8" fill="var(--green)">Made for Pets, Backed by Vets</text>
      <text x="520" y="40" text-anchor="end" class="t-brand" font-size="26" fill="var(--paper)"><tspan font-size="14">Made for </tspan>Pets</text>
      <text x="520" y="72" text-anchor="end" class="t-brand" font-size="26" fill="var(--paper)"><tspan font-size="14">Backed by </tspan>Vets</text>
      <text x="300" y="170" class="t-title" font-size="46" fill="var(--paper)">PET RAPID</text>
      <text x="300" y="228" class="t-title" font-size="56" fill="var(--lime)">TEST KIT</text>
      <rect x="300" y="238" width="196" height="30" fill="none" stroke="var(--lime)" stroke-width="2.5"/>
      <text x="398" y="259" text-anchor="middle" class="t-body" font-weight="700" font-size="15" fill="var(--paper)">FOR DOGS AND CATS</text>
      <text x="232" y="300" class="t-body" font-weight="600" font-size="11" fill="var(--lime)">Contents :</text>
      <g class="t-body" font-size="10.5" fill="var(--paper)">
        <text x="232" y="318">• Test Kits (Cassette, disposable dropper, desiccant)</text>
        <text x="232" y="334">• Assay buffer.</text>
        <text x="232" y="350">• Sterile swabs.</text>
        <text x="232" y="366">• Instruction manual.</text>
      </g>
      <text x="222" y="386" class="t-body" font-size="10" fill="var(--lime)">Store at 2~30C, Avoid direct sunlight</text>
      <g fill="none" stroke="var(--lime)" stroke-width="2.5">
        <circle cx="236" cy="404" r="9"/><circle cx="262" cy="404" r="9"/><circle cx="288" cy="404" r="9"/><circle cx="314" cy="404" r="9"/><circle cx="340" cy="404" r="9"/>
      </g>
      <rect x="440" y="380" width="80" height="28" fill="var(--paper)" stroke="var(--lime)" stroke-width="2"/>
      <rect x="440" y="380" width="80" height="11" fill="var(--lime)"/>
      <text x="480" y="389" text-anchor="middle" class="t-body" font-weight="700" font-size="7.5" fill="var(--paper)">10 Test/Kit</text>
      <text x="480" y="402" text-anchor="middle" class="t-body" font-weight="700" font-size="7.5" fill="var(--ink)">Code No: PS-214</text>
    </svg>
  </section>

</main>
</body>
</html>
```